Flyer Design for Norvane LLC

We need a Flyer for a new company called “Norvane LLC”. This is a technology process improvement company providing a comprehensive assessment of the technology used to run their business. The documentation and review process delivers the visibility and reassurance they need to protect their business and plan for the future. The product is called “Systems Charterwork”. Our primary target is small-medium size businesses, with the deliverables going to the decision maker.

We would like to see the designs use the color blue. Our tag line is "Protect Your Business · Take Control of IT".

- Attached: Norvane LLC Overview document we put together as a starting point. Use as much or as little as you wish.
- Attached: Business Card and Logo designs for colors, etc.

Industry/Entity Type

It Company

```html
<!DOCTYPE html>
<html lang="en">
<head>
<meta charset="utf-8">
<title>Norvane LLC – Systems Charterwork Flyer</title>
<link rel="stylesheet" href="https://fonts.googleapis.com/css2?family=Oswald:wght@500;600&family=Source+Sans+3:wght@400;600;700&family=Montserrat:wght@700&display=swap">
<style>
  :root {
    --blue: #0f6dc9;
    --blue-bright: #1d8fe6;
    --blue-dark: #0a4f9c;
    --blue-soft: #a9bde3;
    --ink: #1d1d1d;
    --paper-gray: #e4e4e4;
    --footer-gray: #6e6e6e;
    --bg: #f1f2f4;
    --white: #ffffff;
  }
  * { box-sizing: border-box; margin: 0; padding: 0; }
  html, body { width: 1200px; height: 1200px; overflow: hidden; background: var(--bg); }
  .canvas { position: relative; width: 1200px; height: 1200px; }
  .flyer {
    position: absolute; left: 150px; top: 18px;
    width: 1006px; height: 1301px;
    transform: scale(0.8946); transform-origin: top left;
    background: linear-gradient(90deg, var(--white) 0%, #f3f3f3 45%, var(--paper-gray) 100%);
    overflow: hidden;
    font-family: "Source Sans 3", "Segoe UI", sans-serif;
    color: var(--ink);
    box-shadow: 0 6px 24px rgba(0,0,0,.15);
  }
  .abs { position: absolute; }
  .header-white { left: 0; top: 0; width: 1006px; height: 240px; background: var(--white); }
  .hero-visual {
    left: 350px; top: 0; width: 656px; height: 498px;
    background:
      radial-gradient(circle at 60% 45%, rgba(180,215,240,.75) 0%, rgba(40,90,150,.5) 30%, rgba(10,25,55,0) 60%),
      linear-gradient(90deg, rgba(255,255,255,1) 0%, rgba(120,150,185,.6) 18%, #1b3558 45%, #0b1a33 100%);
  }
  .brand { left: 68px; top: 130px; display: flex; align-items: center; gap: 14px; }
  .brand-mark { width: 26px; height: 26px; background: var(--blue); }
  .brand-name {
    font-family: "Montserrat", sans-serif; font-weight: 700; font-size: 36px;
    color: var(--blue); letter-spacing: 1px;
  }
  .hero-band { left: 0; top: 228px; width: 560px; height: 282px; }
  .tagline { font-family: "Oswald", "Arial Narrow", sans-serif; font-weight: 500; line-height: 1; text-transform: uppercase; white-space: nowrap; }
  .tagline-top { left: 39px; top: 297px; font-size: 43px; color: var(--white); letter-spacing: -.4px; }
  .tagline-bottom { left: 39px; top: 364px; font-size: 53px; color: var(--ink); letter-spacing: -.5px; }
  .product-name { left: 565px; top: 432px; font-family: "Oswald", sans-serif; font-weight: 500; font-size: 43px; color: var(--white); text-transform: uppercase; letter-spacing: -.5px; white-space: nowrap; }
  h2 { position: absolute; font-weight: 600; font-size: 24px; color: var(--ink); letter-spacing: -.2px; }
  .intro-heading { left: 32px; top: 516px; }
  .intro-text { left: 36px; top: 564px; width: 426px; font-size: 17px; line-height: 22px; text-align: justify; letter-spacing: .35px; }
  .meeting-photo {
    left: 26px; top: 656px; width: 433px; height: 203px;
    border: 2px solid var(--blue);
    background: linear-gradient(100deg, #3a3f48 0%, #c9d4de 35%, #e8edf1 55%, #8d8f93 80%, #3b3027 100%);
  }
  .help-heading { left: 34px; top: 896px; }
  .help-text { left: 36px; top: 936px; width: 428px; font-size: 16.8px; line-height: 21.8px; text-align: justify; letter-spacing: .25px; }
  .areas-heading { left: 563px; top: 521px; }
  .cycle { left: 550px; top: 550px; width: 380px; height: 380px; }
  .cycle text { font-family: "Source Sans 3", sans-serif; font-weight: 700; font-size: 10.5px; fill: var(--white); text-anchor: middle; }
  .dossier-heading { left: 563px; top: 936px; }
  .dossier-list { left: 566px; top: 978px; list-style: none; }
  .dossier-list li { display: flex; align-items: center; gap: 20px; height: 23.6px; font-size: 17px; font-weight: 600; }
  .dossier-list svg { width: 20px; height: 16px; flex: none; }
  .footer-gray { left: 470px; top: 1186px; width: 536px; height: 115px; background: var(--footer-gray); }
  .footer-blue { left: 0; top: 1170px; width: 520px; height: 131px; }
  .contact-heading { left: 38px; top: 1180px; font-size: 24px; font-weight: 600; color: var(--white); }
  .contact-row { display: flex; align-items: center; gap: 10px; font-size: 16.5px; font-weight: 600; color: var(--white); }
  .contact-row svg { width: 20px; height: 20px; fill: var(--ink); flex: none; }
  .contact-name { left: 38px; top: 1216px; }
  .contact-name .role { font-weight: 400; }
  .contact-lines { left: 38px; top: 1242px; gap: 22px; }
  .contact-lines span { display: flex; align-items: center; gap: 10px; }
  .company-lines { left: 565px; top: 1216px; gap: 34px; font-weight: 400; }
  .company-lines span { display: flex; align-items: center; gap: 12px; }
  .website { left: 602px; top: 1242px; font-size: 20px; color: var(--white); letter-spacing: 4.3px; font-weight: 600; }
</style>
</head>
<body>
<div class="canvas">
  <div class="flyer">
    <div class="abs header-white"></div>
    <div class="abs hero-visual" role="img" aria-label="Dark blue technology scene: an open hand holding a laptop surrounded by glowing network nodes, envelopes and a world map"></div>

    <div class="abs brand">
      <span class="brand-mark"></span>
      <span class="brand-name">NORVANE LLC</span>
    </div>

    <svg class="abs hero-band" viewBox="0 0 560 282" aria-hidden="true">
      <defs>
        <linearGradient id="bandFill" x1="0" y1="0" x2="0" y2="1">
          <stop offset="0" stop-color="#1784dc"/>
          <stop offset="1" stop-color="#0d66c2"/>
        </linearGradient>
      </defs>
      <polygon points="0,0 448,0 545,141 448,282 0,282" fill="#ffffff"/>
      <polygon points="0,12 425,12 522,141 425,270 0,270" fill="url(#bandFill)"/>
    </svg>
    <div class="abs tagline tagline-top">Protect Your Business</div>
    <div class="abs tagline tagline-bottom">Take Control of IT</div>
    <div class="abs product-name">Systems Charterwork</div>

    <h2 class="intro-heading">You have big plans, right?</h2>
    <p class="abs intro-text">Technology may help you get there, but how can you plan where you want to go without defining where you are today?</p>
    <div class="abs meeting-photo" role="img" aria-label="Photo of a business team meeting around a glass conference table"></div>

    <h2 class="help-heading">We can help!</h2>
    <p class="abs help-text">Norvane LLC provides a comprehensive assessment of the technology used to run your business. The documentation and review process delivers the visibility and reassurance you need to protect your business. Our team understands that each business operates on its own unique complexities, and crafting a solution requires a custom, unbiased review. Positioning your company with the right insight is intrumental to your success and our goal as your technology partner.</p>

    <h2 class="areas-heading">Evaluating Five Functional Areas</h2>
    <svg class="abs cycle" viewBox="0 0 380 380" aria-label="Cycle of five functional areas">
      <g transform="translate(189,192)">
        <circle r="170" fill="none" stroke="var(--blue-soft)" stroke-width="16"/>
        <circle r="113" fill="none" stroke="var(--blue)" stroke-width="78"/>
        <g stroke="#ffffff" stroke-width="12">
          <line x1="0" y1="-72" x2="0" y2="-178" transform="rotate(8)"/>
          <line x1="0" y1="-72" x2="0" y2="-178" transform="rotate(80)"/>
          <line x1="0" y1="-72" x2="0" y2="-178" transform="rotate(152)"/>
          <line x1="0" y1="-72" x2="0" y2="-178" transform="rotate(224)"/>
          <line x1="0" y1="-72" x2="0" y2="-178" transform="rotate(296)"/>
        </g>
        <g stroke="#9a9a9a" stroke-width="5">
          <line x1="0" y1="-156" x2="0" y2="-178" transform="rotate(8)"/>
          <line x1="0" y1="-156" x2="0" y2="-178" transform="rotate(80)"/>
          <line x1="0" y1="-156" x2="0" y2="-178" transform="rotate(152)"/>
          <line x1="0" y1="-156" x2="0" y2="-178" transform="rotate(224)"/>
          <line x1="0" y1="-156" x2="0" y2="-178" transform="rotate(296)"/>
        </g>
        <circle r="74" fill="#ffffff"/>
        <text x="-75" y="-86">IT</text>
        <text x="-75" y="-73">Administration</text>
        <text x="62" y="-82">IT Service</text>
        <text x="62" y="-69">Delivery</text>
        <text x="112" y="38">Infrastructure</text>
        <text x="112" y="51">Service</text>
        <text x="0" y="126">Application</text>
        <text x="0" y="139">Services</text>
        <text x="-111" y="28">IT Planning</text>
      </g>
    </svg>

    <h2 class="dossier-heading">Dossier Deliverables</h2>
    <ul class="abs dossier-list">
      <li><svg viewBox="0 0 20 16"><rect x="1" y="2" width="16" height="11" fill="none" stroke="#1d8fe6" stroke-width="1.6"/><polyline points="4,10 8,6 11,8 16,3" fill="none" stroke="#1d8fe6" stroke-width="1.6"/></svg>Executive Dashboard</li>
      <li><svg viewBox="0 0 20 16"><rect x="1" y="2" width="16" height="11" fill="none" stroke="#1d8fe6" stroke-width="1.6"/><polyline points="4,10 8,6 11,8 16,3" fill="none" stroke="#1d8fe6" stroke-width="1.6"/></svg>Technology Product Summary</li>
      <li><svg viewBox="0 0 20 16"><rect x="1" y="2" width="16" height="11" fill="none" stroke="#1d8fe6" stroke-width="1.6"/><polyline points="4,10 8,6 11,8 16,3" fill="none" stroke="#1d8fe6" stroke-width="1.6"/></svg>Recommended IT Policies</li>
      <li style="height:20px"><svg viewBox="0 0 20 16"><rect x="1" y="2" width="16" height="11" fill="none" stroke="#1d8fe6" stroke-width="1.6"/><polyline points="4,10 8,6 11,8 16,3" fill="none" stroke="#1d8fe6" stroke-width="1.6"/></svg>Potential Cost Savings</li>
      <li><svg viewBox="0 0 20 16"><rect x="1" y="2" width="16" height="11" fill="none" stroke="#1d8fe6" stroke-width="1.6"/><polyline points="4,10 8,6 11,8 16,3" fill="none" stroke="#1d8fe6" stroke-width="1.6"/></svg>Technology Recommendations</li>
      <li><svg viewBox="0 0 20 16"><rect x="1" y="2" width="16" height="11" fill="none" stroke="#1d8fe6" stroke-width="1.6"/><polyline points="4,10 8,6 11,8 16,3" fill="none" stroke="#1d8fe6" stroke-width="1.6"/></svg>In-depth Questionnaire</li>
      <li><svg viewBox="0 0 20 16"><rect x="1" y="2" width="16" height="11" fill="none" stroke="#1d8fe6" stroke-width="1.6"/><polyline points="4,10 8,6 11,8 16,3" fill="none" stroke="#1d8fe6" stroke-width="1.6"/></svg>Technology Product Details</li>
      <li><svg viewBox="0 0 20 16"><rect x="1" y="2" width="16" height="11" fill="none" stroke="#1d8fe6" stroke-width="1.6"/><polyline points="4,10 8,6 11,8 16,3" fill="none" stroke="#1d8fe6" stroke-width="1.6"/></svg>Full Infrastructure Detailed Report</li>
    </ul>

    <div class="abs footer-gray"></div>
    <svg class="abs footer-blue" viewBox="0 0 520 131" aria-hidden="true">
      <defs>
        <linearGradient id="footFill" x1="0" y1="0" x2="0" y2="1">
          <stop offset="0" stop-color="#1784dc"/>
          <stop offset="1" stop-color="#0d66c2"/>
        </linearGradient>
      </defs>
      <polygon points="0,0 468,0 512,70 468,131 0,131" fill="#ffffff"/>
      <polygon points="0,0 455,0 498,70 455,131 0,131" fill="url(#footFill)"/>
    </svg>
    <div class="abs contact-heading">Contact Info</div>
    <div class="abs contact-row contact-name">
      <svg viewBox="0 0 20 20"><circle cx="10" cy="10" r="9.5"/><circle cx="10" cy="7.5" r="3.2" fill="#fff"/><path d="M4.5 16a5.5 5 0 0 1 11 0z" fill="#fff"/></svg>
      <span>DANIEL ASHFORD <span class="role">(partner)</span></span>
    </div>
    <div class="abs contact-row contact-lines">
      <span><svg viewBox="0 0 20 20"><path d="M5 2l3 3.5-2 2.2a11 11 0 0 0 6.3 6.3l2.2-2L18 15l-2 3C9 17.5 2.5 11 2 4z"/></svg>(866)555-0142</span>
      <span><svg viewBox="0 0 20 20"><rect x="2" y="5" width="16" height="11" fill="none" stroke="#1d1d1d" stroke-width="1.6"/><polyline points="2,5 10,11 18,5" fill="none" stroke="#1d1d1d" stroke-width="1.6"/></svg>dan@norvanellc.com</span>
    </div>
    <div class="abs contact-row company-lines">
      <span><svg viewBox="0 0 20 20"><path d="M5 2l3 3.5-2 2.2a11 11 0 0 0 6.3 6.3l2.2-2L18 15l-2 3C9 17.5 2.5 11 2 4z"/></svg>866-555-0190</span>
      <span><svg viewBox="0 0 20 20"><rect x="2" y="5" width="16" height="11" fill="none" stroke="#1d1d1d" stroke-width="1.6"/><polyline points="2,5 10,11 18,5" fill="none" stroke="#1d1d1d" stroke-width="1.6"/></svg>sales@norvanellc.com</span>
    </div>
    <div class="abs website">www.norvanellc.com</div>
  </div>
</div>
</body>
</html>
```